"Cedar Hollow Realty" is the name of my real estate company

This is for a: "for sale" sign, looking for a minimalist design, wire frame outline of a midcentury modern homes roof line or elevation?

My name is: Marcus Dunleavy (needed)
My Cell # is: 415 382 6094 (needed)
My BRE license # is: 02748156 (needed)
BRE needs to be displayed in this format: BRE 02748156 (needed)
The white outline on the sign riders 'pictured" may work on large sign
Note font on pictured rider sign
Updates

This design is for a real estate "for sale" sign or sandwich board sign. Do Not include the words "For Sale" on the sign.

The measurements are 36" inches (91.44 cm) Length, or tall X 24" inches (60.90 cm) Wide.

|
3
---- 24 ----
6
|

Sorry I wasn't more specific earlier. I'd like the elements of the sign to be scaled in size according to their importance, from largest to smallest:

My name: Marcus Dunleavy
My phone number: 415-382-6094
My company name: Cedar Hollow Realty
My license number: BRE 02748156 (This can be much smaller than the smallest text)
Additionally, please incorporate contemporary to mid-century modern elements on the wire frame roofline or a simple roof-like design.

Thank you!

Best regards,
Marcus

```html
<!DOCTYPE html>
<html lang="en">
<head>
<meta charset="utf-8">
<title>Cedar Hollow Realty – Agent Sign</title>
<link rel="stylesheet" href="https://fonts.googleapis.com/css2?family=Montserrat:wght@700&family=Arimo:wght@400&display=swap">
<style>
  :root {
    --page: #ffffff;
    --board: #1b1c1e;
    --ink: #ffffff;
  }
  html, body {
    margin: 0;
    padding: 0;
    width: 1200px;
    height: 1200px;
    overflow: hidden;
    background: var(--page);
  }
  .sign {
    display: block;
    width: 1200px;
    height: 1200px;
  }
  .board { fill: var(--board); }
  .frame { fill: none; stroke: var(--ink); }
  .brand-name {
    font-family: "Montserrat", sans-serif;
    font-weight: 700;
    font-size: 42px;
    fill: var(--ink);
    text-anchor: middle;
  }
  .copy {
    font-family: "Arimo", Arial, sans-serif;
    font-weight: 400;
    fill: var(--ink);
    text-anchor: middle;
  }
  .brand-license { font-size: 46px; }
  .agent-name { font-size: 44px; }
  .phone-label { font-size: 34px; }
  .phone-number { font-size: 50px; }
  .license-line { font-size: 64px; }
  .license-number { font-size: 66px; }
</style>
</head>
<body>
<svg class="sign" viewBox="0 0 1200 1200" xmlns="http://www.w3.org/2000/svg" role="img" aria-label="Cedar Hollow Realty agent sign">
  <rect class="board" x="17" y="158" width="1166" height="883"/>
  <rect class="frame frame-outer" x="87" y="281" width="1025" height="690" stroke-width="11"/>

  <g class="brand-panel">
    <rect class="frame" x="294" y="339" width="612" height="162" stroke-width="6"/>
    <text class="brand-name" x="600" y="409">CEDAR HOLLOW REALTY</text>
    <text class="copy brand-license" x="600" y="471">BRE 02748156</text>
  </g>

  <g class="agent-panel">
    <rect class="frame" x="167" y="625" width="379" height="301" stroke-width="4"/>
    <text class="copy agent-name" x="356" y="742">Marcus Dunleavy</text>
    <text class="copy phone-label" x="356" y="795">phone number</text>
    <text class="copy phone-number" x="358" y="857">415 382 6094</text>
  </g>

  <g class="license-panel">
    <rect class="frame" x="645" y="626" width="387" height="299" stroke-width="6"/>
    <text class="copy license-line" x="838" y="726">My BRE</text>
    <text class="copy license-line" x="838" y="798">license:</text>
    <text class="copy license-number" x="838" y="870">02748156</text>
  </g>
</svg>
</body>
</html>
```